Real Estate Flyer

I would like an A4 size flyer which has the same info 3 times and can be cut into three.
It will be used for letterbox drops for new listings (SELLING) and sold listings (SOLD). The flyer needs a heading (as above) and a space for a photo which is able to be changed for each new property. Needs to be blue, red and white. It also requires my photo, KLT logo, Marisse Thornbury logo and the following text:
"Are you considering selling? Call Marisse today for a complimentary market appraisal".
(KLT logo, Marisse Thornbury Sales Consultant logo and my photo can be found in uploaded files)
Industry/Entity Type
Real Estate
Look and feel

```html
<!DOCTYPE html>
<html lang="en">
<head>
<meta charset="utf-8">
<title>Marisse Thornbury – Appraisal Flyer</title>
<link rel="stylesheet" href="https://fonts.googleapis.com/css2?family=Hind:wght@300;400&family=Bodoni+Moda:wght@500&display=swap">
<style>
  :root {
    --red: #d8262c;
    --navy: #0f2d5c;
    --paper: #f3f3f3;
    --white: #ffffff;
    --grey-line: #e4e4e4;
    --ink-grey: #8a8a8a;
  }
  * { box-sizing: border-box; margin: 0; padding: 0; }
  html, body { width: 1200px; height: 848px; overflow: hidden; background: var(--white); }
  .sheet { display: flex; width: 1200px; height: 848px; }
  .flyer { position: relative; width: 400px; height: 848px; overflow: hidden; }

  .flyer__hero { position: absolute; inset: 0 0 auto 0; height: 630px; }
  .flyer--red .flyer__hero { background: var(--red); }
  .flyer--navy .flyer__hero { background: var(--navy); }
  .flyer--white .flyer__hero { background: var(--paper); }

  .portrait {
    position: absolute; left: 77px; top: 47px; width: 248px; height: 164px;
    background: linear-gradient(120deg, #b9a57a 0%, #6e6252 45%, #1d1d22 75%, #c9c2a8 100%);
  }
  .flyer--navy .portrait { left: 63px; width: 246px; }
  .flyer--white .portrait { left: 76px; }
  .corner {
    position: absolute; width: 56px; height: 56px; border-radius: 50%;
    background: rgba(255,255,255,0.28);
  }
  .corner--tl { left: -28px; top: -28px; }
  .corner--br { right: -28px; bottom: -28px; }

  .pitch {
    position: absolute; left: 32px; top: 238px; width: 360px;
    font-family: "Hind", sans-serif; font-weight: 300; font-size: 36px; line-height: 54.5px;
    color: var(--white);
  }
  .flyer--navy .pitch { left: 30px; }
  .flyer--white .pitch { left: 30px; color: var(--red); }
  .pitch__call { padding-left: 6px; }
  .pitch__name {
    display: block; font-family: "Bodoni Moda", serif; font-weight: 500;
    font-size: 56px; line-height: 54px; letter-spacing: -1px; color: var(--navy);
  }
  .flyer--navy .pitch__name { color: var(--red); }

  .flyer__rule { position: absolute; left: 0; right: 0; top: 630px; height: 8px; }
  .flyer--red .flyer__rule { background: var(--grey-line); }
  .flyer--navy .flyer__rule { background: var(--red); }
  .flyer--white .flyer__rule { background: var(--navy); }

  .agent {
    position: absolute; left: 0; right: 0; top: 638px; height: 134px; background: var(--white);
  }
  .agent__mark {
    position: absolute; left: 84px; top: 44px; width: 40px; height: 40px; border-radius: 50%;
    background: var(--red);
  }
  .flyer--navy .agent__mark { left: 487px; left: 87px; }
  .agent__name {
    position: absolute; left: 130px; top: 44px;
    font-family: "Hind", sans-serif; font-weight: 400; font-size: 19px; letter-spacing: 1px;
    color: #333;
  }
  .agent__role {
    position: absolute; left: 175px; top: 67px;
    font-family: "Hind", sans-serif; font-weight: 300; font-size: 13px; letter-spacing: 1px; color: var(--ink-grey);
  }
  .agent__phone {
    position: absolute; left: 197px; top: 85px;
    font-family: "Hind", sans-serif; font-weight: 400; font-size: 14px; color: var(--red);
  }

  .flyer__footer { position: absolute; left: 0; right: 0; top: 772px; height: 76px; }
  .flyer--red .flyer__footer { background: linear-gradient(180deg, #a11a1e, #6d1013); }
  .flyer--navy .flyer__footer { background: linear-gradient(180deg, #132c55, #0a1a36); }
  .flyer--white .flyer__footer { background: linear-gradient(180deg, #9a9a9a, #6a6a6a); }
  .brand {
    position: absolute; left: 125px; top: 24px; width: 152px; height: 26px;
    background: var(--navy); border: 2px solid var(--white);
    display: flex; align-items: center; justify-content: center;
    font-family: "Hind", sans-serif; font-weight: 400; font-size: 16px; letter-spacing: 2px; color: var(--white);
  }
</style>
</head>
<body>
<main class="sheet">

  <section class="flyer flyer--red">
    <div class="flyer__hero">
      <div class="portrait" role="img" aria-label="Portrait photo of Marisse Thornbury at a verandah"></div>
    </div>
    <p class="pitch">"Are you considering selling?<br><span class="pitch__call">Call</span><span class="pitch__name">Marisse</span>today for a complimentary market appraisal".</p>
    <div class="flyer__rule"></div>
    <div class="agent">
      <span class="agent__mark"></span>
      <span class="agent__name">Marisse Thornbury</span>
      <span class="agent__role">Sales Consultant</span>
      <span class="agent__phone">0400 555 218</span>
    </div>
    <div class="flyer__footer" role="img" aria-label="Red-tinted photo of a house facade">
      <span class="brand">KLT</span>
    </div>
  </section>

  <section class="flyer flyer--navy">
    <div class="flyer__hero">
      <div class="portrait" role="img" aria-label="Portrait photo of Marisse Thornbury at a verandah"></div>
    </div>
    <p class="pitch">"Are you considering selling?<br><span class="pitch__call">Call</span><span class="pitch__name">Marisse</span>today for a complimentary market appraisal".</p>
    <div class="flyer__rule"></div>
    <div class="agent">
      <span class="agent__mark"></span>
      <span class="agent__name">Marisse Thornbury</span>
      <span class="agent__role">Sales Consultant</span>
      <span class="agent__phone">0400 555 218</span>
    </div>
    <div class="flyer__footer" role="img" aria-label="Blue-tinted photo of a house facade">
      <span class="brand">KLT</span>
    </div>
  </section>

  <section class="flyer flyer--white">
    <div class="flyer__hero">
      <div class="portrait" role="img" aria-label="Portrait photo of Marisse Thornbury at a verandah"></div>
    </div>
    <p class="pitch">"Are you considering selling?<br><span class="pitch__call">Call</span><span class="pitch__name">Marisse</span>today for a complimentary market appraisal".</p>
    <div class="flyer__rule"></div>
    <div class="agent">
      <span class="agent__mark"></span>
      <span class="agent__name">Marisse Thornbury</span>
      <span class="agent__role">Sales Consultant</span>
      <span class="agent__phone">0400 555 218</span>
    </div>
    <div class="flyer__footer" role="img" aria-label="Greyscale photo of a stone house facade">
      <span class="brand">KLT</span>
    </div>
  </section>

</main>
</body>
</html>
```